Thornwell Building Company - advertisement poster

I am looking to print some canvas signs to advertise my general contracting company, Thornwell Building Company. The sign will measure 6' long x 3' high so the size should match that ratio. I already have a logo icon, which is the Letter 'A' and some trees that I would like to incorporate, see attached. I would also like the to have the following information listed:
1) phone number: 472-318-6095
2) email: thornwellbuildingcompany@mailvistra.net
3) website: thornwellbuildingcompany.com
4) Lic#5386204
5) I want to use this text: "BUILD WITH THE T-CREW!"

The ad should be relatively simple and clean. Black and Green are my company colors. I am open to creative ideas!

Target Market(s)

People looking to renovate their homes

Industry/Entity Type

Construction

Colors
59FF00
82FF00
B8FF75
E3FFCB
F4FFEA

Requirements
Must have
• Must have my company logo
Should not have
• No photos or complex graphics

```html
<!DOCTYPE html>
<html lang="en">
<head>
<meta charset="utf-8">
<title>Thornwell Building Company – Canvas Sign</title>
<link rel="stylesheet" href="https://fonts.googleapis.com/css2?family=Montserrat:ital,wght@0,600;0,700;0,800;1,700&family=Oswald:wght@500;600&display=swap">
<style>
  :root {
    --green: #6ab63f;
    --green-dark: #4a8a2c;
    --ink: #0d0d0d;
    --paper: #ffffff;
    --backdrop: #cfcfcf;
    --tool: #2a2a2a;
  }
  html, body {
    margin: 0;
    padding: 0;
    width: 844px;
    height: 1200px;
    overflow: hidden;
    background: var(--backdrop);
  }
  .sign {
    position: absolute;
    left: 32px;
    top: 405px;
    width: 780px;
    height: 395px;
    display: block;
    box-shadow: 0 2px 6px rgba(0,0,0,0.18);
  }
  .headline { font-family: "Oswald", "Arial Narrow", sans-serif; font-weight: 600; fill: var(--ink); }
  .headline--accent { fill: var(--green); }
  .licence { font-family: "Oswald", "Arial Narrow", sans-serif; font-weight: 500; fill: var(--ink); }
  .company-name { font-family: "Montserrat", Arial, sans-serif; font-weight: 700; fill: var(--paper); }
  .contact-label { font-family: "Montserrat", Arial, sans-serif; font-weight: 800; fill: var(--ink); }
  .phone-number { font-family: "Montserrat", Arial, sans-serif; font-weight: 600; fill: var(--paper); }
  .link-text { font-family: "Montserrat", Arial, sans-serif; font-weight: 700; font-style: italic; fill: var(--paper); }
  .underline { stroke: var(--paper); stroke-width: 2; }
</style>
</head>
<body>
<svg class="sign" viewBox="0 0 1239 628" xmlns="http://www.w3.org/2000/svg" aria-label="Thornwell Building Company canvas sign">
  <!-- background -->
  <rect class="sign__paper" x="0" y="0" width="1239" height="628" fill="var(--paper)"/>

  <!-- brand panel -->
  <g class="brand-panel">
    <rect x="44" y="0" width="398" height="306" fill="var(--green)"/>
    <rect x="50" y="34" width="386" height="264" fill="var(--ink)"/>
    <rect class="brand-mark" x="215" y="92" width="56" height="56" fill="var(--green)"/>
    <text class="company-name" x="243" y="205" font-size="44" text-anchor="middle" textLength="318" lengthAdjust="spacingAndGlyphs">THORNWELL</text>
    <text class="company-name" x="243" y="240" font-size="20" text-anchor="middle" textLength="318" lengthAdjust="spacing">BUILDING COMPANY</text>
    <rect class="licence-tab" x="110" y="290" width="267" height="38" fill="var(--green)"/>
    <text class="licence" x="243" y="319" font-size="26" text-anchor="middle" textLength="230" lengthAdjust="spacingAndGlyphs">LICENCE ID - 5386204</text>
  </g>

  <!-- house frame with headline -->
  <g class="house-frame">
    <path d="M570 351 V161 H488 L830 26 L1177 161 H1097 V351"
          fill="none" stroke="var(--green)" stroke-width="14" stroke-linejoin="miter"/>
    <rect x="563" y="344" width="541" height="14" fill="var(--green)"/>
    <rect class="hammer" role="img" aria-label="Hammer icon" x="765" y="70" width="105" height="40" rx="8" fill="var(--tool)" transform="rotate(-12 817 90)"/>
    <text class="headline" x="667" y="250" font-size="130" textLength="215" lengthAdjust="spacingAndGlyphs">BUILD</text>
    <text class="headline" x="905" y="196" font-size="56" textLength="92" lengthAdjust="spacingAndGlyphs">WITH</text>
    <text class="headline" x="905" y="250" font-size="56" textLength="72" lengthAdjust="spacingAndGlyphs">THE</text>
    <text class="headline headline--accent" x="645" y="330" font-size="100" textLength="380" lengthAdjust="spacingAndGlyphs">T-CREW!</text>
  </g>

  <!-- contact band -->
  <g class="contact-band">
    <rect x="0" y="358" width="1239" height="270" fill="var(--ink)"/>

    <polygon class="cta-arrow__shade" points="462,370 517,447 462,523 448,523 448,370" fill="var(--green-dark)"/>
    <rect class="cta-arrow" x="50" y="390" width="412" height="113" fill="var(--green)"/>
    <polygon class="cta-arrow__head" points="448,390 502,447 448,503" fill="var(--green)"/>
    <text class="contact-label" x="87" y="465" font-size="44" textLength="323" lengthAdjust="spacingAndGlyphs">CONTACT US</text>

    <circle class="phone-badge" cx="605" cy="448" r="55" fill="var(--green)"/>
    <path class="phone-icon" d="M586 422 c5 -3 10 -2 12 3 l6 12 c2 4 0 8 -4 10 l-5 3 c3 8 10 15 18 18 l3 -5 c2 -4 6 -6 10 -4 l12 6 c5 2 6 7 3 12 l-4 6 c-4 5 -10 7 -17 5 c-22 -7 -40 -25 -47 -47 c-2 -7 0 -13 5 -17 z" fill="var(--ink)"/>
    <path d="M616 424 a14 14 0 0 1 14 14 M616 413 a25 25 0 0 1 25 25" fill="none" stroke="var(--ink)" stroke-width="4" stroke-linecap="round"/>
    <text class="phone-number" x="692" y="474" font-size="70" textLength="492" lengthAdjust="spacingAndGlyphs">472-318-6095</text>

    <g class="web-link">
      <circle cx="119" cy="560" r="23" fill="none" stroke="var(--green)" stroke-width="3"/>
      <circle cx="119" cy="560" r="11" fill="none" stroke="var(--green)" stroke-width="2"/>
      <ellipse cx="119" cy="560" rx="5" ry="11" fill="none" stroke="var(--green)" stroke-width="1.5"/>
      <line x1="108" y1="560" x2="130" y2="560" stroke="var(--green)" stroke-width="1.5"/>
      <text class="link-text" x="169" y="566" font-size="19" textLength="388" lengthAdjust="spacingAndGlyphs">THORNWELLBUILDINGCOMPANY.COM</text>
      <line class="underline" x1="169" y1="576" x2="557" y2="576"/>
    </g>

    <g class="email-link">
      <circle cx="622" cy="560" r="23" fill="none" stroke="var(--green)" stroke-width="3"/>
      <rect x="611" y="553" width="22" height="15" fill="none" stroke="var(--green)" stroke-width="2"/>
      <polyline points="611,553 622,562 633,553" fill="none" stroke="var(--green)" stroke-width="2"/>
      <text class="link-text" x="669" y="566" font-size="17" textLength="476" lengthAdjust="spacingAndGlyphs">THORNWELLBUILDINGCOMPANY@MAILVISTRA.NET</text>
      <line class="underline" x1="669" y1="576" x2="1145" y2="576"/>
    </g>
  </g>
</svg>
</body>
</html>
```